Welding company needs a business card

We are looking for a logo and business card.

Contact Information for Business Card

418 Cobblestone Lane
York, PA 17402
410-555-0173
Rmfabworksco@quorvamail.com

```html
<!DOCTYPE html>
<html lang="en">
<head>
<meta charset="utf-8">
<title>R&amp;M Fabworks Co — Business Card</title>
<link rel="stylesheet" href="https://fonts.googleapis.com/css2?family=Jost:wght@400;500;700&display=swap">
<style>
  :root {
    --canvas: #eeeeee;
    --charcoal: #2e2e2e;
    --charcoal-stripe: #363636;
    --paper: #fafafa;
    --paper-stripe: #f0f0f0;
    --ink: #454545;
    --ink-soft: #9a9a9a;
    --white: #ffffff;
    --yellow: #ffc800;
    --amber: #f5922f;
    --orange: #ef6a35;
    --red: #ec3b2f;
  }
  * { margin: 0; padding: 0; box-sizing: border-box; }
  html, body { width: 1200px; height: 957px; overflow: hidden; background: var(--canvas); }
  body { position: relative; font-family: "Jost", sans-serif; }

  .card { position: absolute; left: 266px; width: 674px; height: 384px; overflow: hidden; }
  .card--front { top: 50px;
    background: repeating-linear-gradient(90deg, var(--charcoal) 0 12px, var(--charcoal-stripe) 12px 22px, var(--charcoal) 22px 27px); }
  .card--back { top: 516px;
    background: repeating-linear-gradient(90deg, var(--paper) 0 12px, var(--paper-stripe) 12px 22px, var(--paper) 22px 27px); }

  .card__band { position: absolute; left: 0; top: 0; width: 674px; height: 384px; }

  .brand { position: absolute; left: 0; right: 0; top: 0; text-align: center; }
  .brand__dot { position: absolute; left: 295px; top: 81px; width: 82px; height: 82px; border-radius: 50%; }
  .card--front .brand__dot { background: var(--white); }
  .card--back .brand__dot { background: var(--charcoal); }

  .brand__name { position: absolute; left: 0; right: 0; top: 178px; font-size: 36px; font-weight: 700; letter-spacing: 1.5px; line-height: 1; }
  .brand__rule { position: absolute; left: 178px; width: 312px; top: 224px; height: 2px; }
  .brand__tagline { position: absolute; left: 0; right: 0; top: 231px; font-size: 23px; font-weight: 400; letter-spacing: 0.8px; line-height: 1; }

  .card--front .brand__name, .card--front .brand__tagline { color: var(--white); }
  .card--front .brand__rule { background: var(--white); }
  .card--back .brand__name { color: var(--ink); }
  .card--back .brand__rule { background: var(--ink); }
  .card--back .brand__tagline { color: var(--ink-soft); }

  .contact { position: absolute; top: 280px; display: flex; align-items: center; gap: 10px; font-size: 20px; color: #2a2a2a; letter-spacing: 0.3px; }
  .contact--phone { left: 66px; }
  .contact--email { left: 335px; }
  .contact svg { display: block; }

  .address { position: absolute; left: 0; right: 0; top: 345px; text-align: center; color: var(--white); font-size: 18px; font-weight: 500; letter-spacing: 0.6px; }

  .swatch { position: absolute; left: 64px; width: 53px; height: 53px; border-radius: 50%; }
  .swatch--yellow { top: 517px; background: var(--yellow); }
  .swatch--amber { top: 583px; background: var(--amber); }
  .swatch--orange { top: 648px; background: var(--orange); }
  .swatch--red { top: 713px; background: var(--red); }
  .swatch--white { top: 779px; background: var(--white); }
  .swatch--charcoal { top: 844px; background: var(--charcoal); }
</style>
</head>
<body>
  <svg width="0" height="0" style="position:absolute">
    <defs>
      <linearGradient id="flame" x1="0" y1="0" x2="1" y2="0">
        <stop offset="0" stop-color="#ec3b2f"/>
        <stop offset="0.35" stop-color="#ef6a35"/>
        <stop offset="0.7" stop-color="#f4932f"/>
        <stop offset="0.85" stop-color="#f9a800"/>
        <stop offset="1" stop-color="#ffc800"/>
      </linearGradient>
    </defs>
  </svg>

  <section class="card card--front">
    <svg class="card__band" viewBox="0 0 674 384"><polygon points="0,269 54,319 620,319 674,269 674,384 0,384" fill="url(#flame)"/></svg>
    <div class="brand">
      <div class="brand__dot"></div>
      <div class="brand__name">R&amp;M FABWORKS CO</div>
      <div class="brand__rule"></div>
      <div class="brand__tagline">Mobile Welding &amp; Fabrication</div>
    </div>
  </section>

  <section class="card card--back">
    <svg class="card__band" viewBox="0 0 674 384"><polygon points="0,269 54,319 620,319 674,269 674,384 0,384" fill="url(#flame)"/></svg>
    <div class="brand">
      <div class="brand__dot"></div>
      <div class="brand__name">R&amp;M FABWORKS CO</div>
      <div class="brand__rule"></div>
      <div class="brand__tagline">Mobile Welding &amp; Fabrication</div>
    </div>
    <div class="contact contact--phone">
      <svg width="18" height="30" viewBox="0 0 18 30" fill="none" stroke="#ef6a35" stroke-width="1.4"><rect x="1" y="1" width="16" height="28" rx="2.5"/><line x1="1" y1="5" x2="17" y2="5"/><line x1="1" y1="23" x2="17" y2="23"/><circle cx="9" cy="26" r="1"/></svg>
      <span>410-555-0173</span>
    </div>
    <div class="contact contact--email">
      <svg width="32" height="22" viewBox="0 0 32 22" fill="none" stroke="#ef6a35" stroke-width="1.4"><rect x="1" y="1" width="30" height="20"/><polyline points="1,1 16,13 31,1"/><line x1="1" y1="21" x2="12" y2="10"/><line x1="31" y1="21" x2="20" y2="10"/></svg>
      <span>Rmfabworksco@quorvamail.com</span>
    </div>
    <div class="address">418 Cobblestone Lane, York, PA 17402</div>
  </section>

  <div class="swatch swatch--yellow"></div>
  <div class="swatch swatch--amber"></div>
  <div class="swatch swatch--orange"></div>
  <div class="swatch swatch--red"></div>
  <div class="swatch swatch--white"></div>
  <div class="swatch swatch--charcoal"></div>
</body>
</html>
```